Migration Lawyers

Company: Dunstan & Co Lawyers & Migration Agents

Name: Graham Dunstan BEc, LLB
Address: Level 18, 72 Hollis Street
Sydney, NSW, Australia 2000

Ph: +61 2 9384 5207
M: 0428316540
E: graham@permitpath-example.org.au
W: www.permitpath-example.org.au

Target Market(s)

Migration Clients

Industry/Entity Type

It Company

Font styles to use
Script

Requirements
Must have
• Logo
Should not have
• Please scale the format to the printing size attached

```html
<!DOCTYPE html>
<html lang="en">
<head>
<meta charset="utf-8">
<title>Dunstan &amp; Co — Business Cards</title>
<link rel="stylesheet" href="https://fonts.googleapis.com/css2?family=Pinyon+Script&family=Libre+Baskerville:wght@400;700&display=swap">
<style>
  :root {
    --backdrop: #d4d4d6;
    --backdrop-deep: #a9a9ac;
    --card-white: #fbfbfb;
    --card-black: #0b0b0b;
    --ink: #141414;
    --ink-soft: #9a9a9a;
    --paper-text: #f2f2f2;
    --ring: #8c8c8c;
  }
  * { margin: 0; padding: 0; box-sizing: border-box; }
  html, body { width: 1200px; height: 900px; overflow: hidden; }
  body {
    background: radial-gradient(ellipse at 50% 35%, var(--backdrop) 0%, var(--backdrop-deep) 100%);
    font-family: "Libre Baskerville", Georgia, serif;
    position: relative;
  }
  .card {
    position: absolute;
    top: 295px;
    width: 540px;
    height: 310px;
    border-radius: 3px;
    box-shadow: 0 18px 40px rgba(0,0,0,.28);
    overflow: hidden;
  }
  .card--front { left: 40px; background: var(--card-white); }
  .card--back { left: 620px; background: var(--card-black); color: var(--paper-text); }

  /* Front: wordmark */
  .wordmark {
    position: absolute;
    left: 70px; top: 100px;
    display: flex; align-items: center; gap: 22px;
  }
  .wordmark__ring {
    width: 104px; height: 104px;
    border: 2px solid var(--ring);
    border-radius: 50%;
    flex: none;
  }
  .wordmark__text { color: var(--ink); font-weight: 700; line-height: 1.15; }
  .wordmark__name { font-size: 38px; display: block; }
  .wordmark__tag { font-size: 15px; display: block; letter-spacing: .3px; }

  /* Back: details */
  .back-mark {
    position: absolute; top: 22px; left: 0; right: 0;
    display: flex; justify-content: center; align-items: center; gap: 8px;
    font-size: 11px; font-weight: 700; color: var(--ink-soft);
  }
  .back-mark__ring { width: 34px; height: 34px; border: 1.5px solid var(--ink-soft); border-radius: 50%; }
  .holder {
    position: absolute; top: 84px; left: 0; right: 0; text-align: center;
    font-family: "Pinyon Script", cursive; font-size: 34px; color: #fff;
  }
  .address {
    position: absolute; top: 136px; left: 250px;
    font-size: 11px; line-height: 1.45; color: var(--paper-text);
  }
  .contacts { position: absolute; list-style: none; font-size: 11px; }
  .contacts li { display: flex; align-items: center; gap: 10px; margin-bottom: 9px; }
  .contacts svg { width: 13px; height: 13px; flex: none; }
  .contacts--web { top: 190px; left: 290px; }
  .contacts--phone { top: 236px; left: 32px; }
</style>
</head>
<body>
  <section class="card card--front" aria-label="Card front">
    <div class="wordmark">
      <span class="wordmark__ring"></span>
      <span class="wordmark__text">
        <span class="wordmark__name">Dunstan &amp; Co</span>
        <span class="wordmark__tag">Lawyers &amp; Migration Agents</span>
      </span>
    </div>
  </section>

  <section class="card card--back" aria-label="Card back">
    <div class="back-mark"><span class="back-mark__ring"></span><span>Dunstan &amp; Co</span></div>
    <h1 class="holder">Graham Dunstan BEc, LLB</h1>
    <p class="address">Level 18, 72 Hollis Street<br>Australia, Sydney, NSW, 2000</p>

    <ul class="contacts contacts--web">
      <li>
        <svg viewBox="0 0 14 14" fill="none" stroke="#fff" stroke-width="1.2"><rect x="1" y="3" width="12" height="8"/><path d="M1 3l6 5 6-5"/></svg>
        graham@permitpath-example.org.au
      </li>
      <li>
        <svg viewBox="0 0 14 14" fill="none" stroke="#fff" stroke-width="1.2"><rect x="1.5" y="2" width="11" height="8"/><path d="M4 12.5h6"/></svg>
        www.permitpath-example.org.au
      </li>
    </ul>

    <ul class="contacts contacts--phone">
      <li>
        <svg viewBox="0 0 14 14" fill="#fff"><path d="M3 1.5l2 2.2-1 1.5c.8 1.8 2 3 3.8 3.8l1.5-1 2.2 2-1.2 2C6 11.8 2.2 8 1.3 2.7z"/></svg>
        +61 2 9384 5207
      </li>
      <li>
        <svg viewBox="0 0 14 14" fill="none" stroke="#fff" stroke-width="1.2"><rect x="3.5" y="1" width="7" height="12" rx="1"/><path d="M6 11h2"/></svg>
        0428316540
      </li>
    </ul>
  </section>
</body>
</html>
```